"Grandpa's Old Mule" Bookcover 170501

We need a book cover for print edition of the title, "Grandpa's Old Mule". The book is about the life of a man and that of his last dog, told from the perspective of his son. The book is a mix of highly improbable situations and a son's remembrance of his father. We've attached pictures of both the man and the dog, however, they do not have to be used, if it doesn't add to the design. It does provide an idea of what the subjects looked like. The author's name is Rob T. Venster. The publisher will be Quiet Heron Publishers. One book size template uploaded. NOTE: Designer credit will be included in the published work.

Target Market(s)

People who like non-fiction strange family and dog stories

Font styles to use
Serif
Sans Serif

Colors

Designer to choose colors to be used in the design.

Requirements
Must have
• A means of communicating a story about two lifetimes, the man and the dog. Full cover, front, spine and back.
Nice to have
• Man and Dog get equal billing, something that indicates a lifetime of events
Should not have
• A mere collage of the uploaded pics. Those can be used, but don't make it as simple as a photo album.

```html
<!DOCTYPE html>
<html lang="en">
<head>
<meta charset="utf-8">
<title>Grandpa's Old Mule — Full Cover</title>
<link href="https://fonts.googleapis.com/css2?family=Cinzel:wght@400;600&family=EB+Garamond:wght@500;700&family=Montserrat:wght@400&display=swap" rel="stylesheet">
<style>
  :root {
    --sky-top: #c9701a;
    --sky-mid: #e59a22;
    --sky-glow: #f2b13a;
    --sky-low: #d9561c;
    --ground: #060505;
    --spine: #4a1f1c;
    --ink-light: #ffffff;
    --title-shadow: rgba(40, 15, 5, 0.85);
  }
  html, body {
    margin: 0;
    padding: 0;
    width: 1200px;
    height: 859px;
    overflow: hidden;
    background: #ffffff;
  }
  .cover-wrap {
    position: relative;
    width: 1200px;
    height: 859px;
    overflow: hidden;
    background:
      radial-gradient(ellipse 260px 140px at 700px 705px, rgba(255, 240, 120, 0.95), rgba(255, 200, 60, 0.5) 45%, rgba(255, 160, 40, 0) 100%),
      radial-gradient(ellipse 700px 420px at 760px 600px, rgba(240, 150, 40, 0.6), rgba(240, 150, 40, 0) 100%),
      linear-gradient(180deg, var(--sky-top) 0%, var(--sky-mid) 30%, var(--sky-glow) 52%, var(--sky-low) 78%, #b8401a 84%);
  }
  .sky-scene {
    position: absolute;
    inset: 0;
  }
  .ground {
    position: absolute;
    left: 0;
    right: 0;
    top: 718px;
    bottom: 0;
    background: var(--ground);
  }
  .silhouette-art {
    position: absolute;
    left: 732px;
    top: 440px;
    width: 336px;
    height: 290px;
    background: linear-gradient(180deg, rgba(6, 5, 5, 0.55) 0%, rgba(6, 5, 5, 0.9) 70%, var(--ground) 100%);
    border-radius: 120px 120px 0 0;
  }

  /* Back cover */
  .back-cover {
    position: absolute;
    left: 0;
    top: 0;
    width: 574px;
    height: 859px;
  }
  .back-title {
    position: absolute;
    left: 0;
    width: 552px;
    top: 128px;
    margin: 0;
    text-align: center;
    font-family: "Cinzel", serif;
    font-weight: 400;
    font-size: 25px;
    letter-spacing: 0.5px;
    color: var(--ink-light);
  }
  .back-blurb {
    position: absolute;
    left: 64px;
    top: 222px;
    width: 452px;
    margin: 0;
    font-family: "Montserrat", sans-serif;
    font-size: 13.6px;
    line-height: 19.2px;
    color: var(--ink-light);
    hyphens: auto;
  }

  /* Spine */
  .spine {
    position: absolute;
    left: 574px;
    top: 0;
    width: 52px;
    height: 859px;
    background: var(--spine);
    color: var(--ink-light);
  }
  .spine-title,
  .spine-author {
    position: absolute;
    left: 0;
    width: 52px;
    margin: 0;
    writing-mode: vertical-rl;
    display: flex;
    align-items: center;
  }
  .spine-title {
    top: 46px;
    font-family: "Cinzel", serif;
    font-weight: 400;
    font-size: 25px;
  }
  .spine-author {
    top: 652px;
    font-family: "EB Garamond", serif;
    font-weight: 500;
    font-size: 24px;
  }

  /* Front cover */
  .front-cover {
    position: absolute;
    left: 626px;
    top: 0;
    width: 574px;
    height: 859px;
  }
  .front-title {
    position: absolute;
    left: 40px;
    width: 510px;
    top: 22px;
    margin: 0;
    text-align: center;
    font-family: "Cinzel", serif;
    font-weight: 600;
    color: var(--ink-light);
    text-shadow: 2px 3px 2px var(--title-shadow);
  }
  .front-title .line {
    display: block;
  }
  .front-title .line-long {
    font-size: 76px;
    line-height: 120px;
  }
  .front-title .line-short {
    font-size: 122px;
    line-height: 132px;
  }
  .front-author {
    position: absolute;
    left: 0;
    width: 584px;
    top: 766px;
    margin: 0;
    text-align: center;
    font-family: "EB Garamond", serif;
    font-weight: 700;
    font-size: 41px;
    color: var(--ink-light);
  }
</style>
</head>
<body>
  <main class="cover-wrap">
    <div class="sky-scene" role="img" aria-label="Sunset sky over a grassy horizon with scattered tree silhouettes"></div>
    <div class="ground"></div>
    <div class="silhouette-art" role="img" aria-label="Silhouette of a man sitting beside his dog against the setting sun"></div>

    <section class="back-cover">
      <h2 class="back-title">Grandpa's Old Mule</h2>
      <p class="back-blurb">Lorem ipsum dolor sit amet, consectetuer adipiscing elit. Aenean commodo ligula eget dolor. Aenean massa. Cum sociis natoque penatibus et magnis dis parturient montes, nascetur ridiculus mus. Donec quam felis, ultricies nec, pellentesque eu, pretium quis, sem. Nulla consequat massa quis enim. Donec pede justo, fringilla vel, aliquet nec, vulputate eget, arcu. In enim justo, rhoncus ut, imperdiet a, venenatis vitae, justo. Nullam dictum felis eu pede mollis pretium. Integer tincidunt. Cras dapibus. Vivamus elementum semper nisi. Aenean vulputate eleifend tellus.</p>
    </section>

    <section class="spine">
      <p class="spine-title">Grandpa's Old Mule</p>
      <p class="spine-author">Rob T. Venster</p>
    </section>

    <section class="front-cover">
      <h1 class="front-title">
        <span class="line line-long">Grandpa's</span>
        <span class="line line-short">Old</span>
        <span class="line line-short">Mule</span>
      </h1>
      <p class="front-author">Rob T. Venster</p>
    </section>
  </main>
</body>
</html>
```